Business Card needed for International Migration and Education business

we are based in Australia, the business is called 'FarReach Relocation' and its sister business for international education is called 'FarReach Learning' - we need the design for the business 'FarReach Relocation' - FarReach Relocation is about migration to Australia (but not limited to Australia only therefore purely Australian look would not fit). We would like to see designs that use the color blue or acqua and maybe orange..all those colours don't have to be used together and not only those colours are to be used. We are looking for a modern design. The final design should communicate modern thinking, professionalism, dynamism, confidence. We would like to use the same business card design for our sister business "FarReach Learning" - which is business about studying in different countries as we recruit students to study in Australia, USA, New Zealand, Canada, UK etc. We would like to be able the final design to be easily changed by us to fit the 'FarReach Learning' business - we would only change the contact text (email address etc)

The information to be included in the business card: Tessa Virnaud Managing Director Migration Agent MARN 0917264 FarReach Relocation postal address: PO Box 2749, Carlwood East VIC 3179, Australia mobile: 0417296031 office address: Level 1, 287 Fenwick Road, Ardmere VIC 3211 web www.farreachrelocation-example.com telephone: 61 3 8714 6023 fax + 61 3 8735 2910 email: tessa@farreachrelocation-example.com

```html
<!DOCTYPE html>
<html lang="en">
<head>
<meta charset="utf-8">
<title>FarReach Relocation – Business Card</title>
<link rel="stylesheet" href="https://fonts.googleapis.com/css2?family=Arimo:wght@400&display=swap">
<style>
  :root {
    --navy-deep: #020a1c;
    --navy: #06203f;
    --ocean: #0b5d86;
    --aqua: #29b6d8;
    --aqua-light: #9fe6f5;
    --glow: #e6fbff;
    --ink-dark: #0a0f1e;
    --ink-light: #ffffff;
    --globe-blue: #1f5fa8;
    --globe-cloud: #dfe9f3;
  }
  html, body {
    margin: 0;
    padding: 0;
    width: 1200px;
    height: 702px;
    overflow: hidden;
    background: #ffffff;
  }
  .card {
    position: relative;
    width: 1200px;
    height: 702px;
    overflow: hidden;
    font-family: "Arimo", Arial, sans-serif;
  }
  .card-backdrop {
    position: absolute;
    inset: 0;
    background:
      radial-gradient(ellipse 520px 320px at 960px 170px, var(--glow) 0%, var(--aqua-light) 30%, rgba(41,182,216,0) 75%),
      radial-gradient(ellipse 700px 420px at 520px 250px, rgba(41,182,216,0.85) 0%, rgba(11,93,134,0.7) 45%, rgba(6,32,63,0) 80%),
      radial-gradient(ellipse 420px 300px at 860px 520px, rgba(41,182,216,0.55) 0%, rgba(6,32,63,0) 75%),
      linear-gradient(160deg, var(--navy) 0%, var(--ocean) 35%, var(--navy) 65%, var(--navy-deep) 100%);
  }
  .globe {
    position: absolute;
    left: 937px;
    top: 448px;
    width: 264px;
    height: 264px;
    border-radius: 50%;
    background:
      radial-gradient(circle at 35% 30%, var(--globe-cloud) 0%, rgba(223,233,243,0.4) 22%, rgba(31,95,168,0) 45%),
      radial-gradient(circle at 45% 45%, var(--globe-blue) 0%, #123a78 60%, #081a3c 100%);
    box-shadow: 0 0 18px rgba(159,230,245,0.35);
  }
  .holder {
    position: absolute;
    right: 78px;
    top: 52px;
    text-align: right;
    color: var(--ink-dark);
  }
  .holder-name {
    margin: 0;
    font-size: 40px;
    font-weight: 400;
    line-height: 1;
    letter-spacing: 0.2px;
  }
  .holder-title {
    margin: 8px 0 0;
    font-size: 33px;
    font-weight: 400;
    line-height: 1.1;
  }
  .contact {
    position: absolute;
    left: 65px;
    top: 338px;
    margin: 0;
    padding: 0;
    list-style: none;
    color: var(--ink-light);
    font-size: 23.5px;
    line-height: 33px;
    text-shadow: 0 0 4px rgba(2,10,28,0.6);
  }
  .contact li { white-space: nowrap; }
  .contact .gap-before { margin-top: 6px; }
</style>
</head>
<body>
  <main class="card">
    <div class="card-backdrop" role="img" aria-label="Glowing blue world map with light trails connecting cities across continents"></div>
    <div class="globe" role="img" aria-label="Photograph of planet Earth seen from space"></div>

    <header class="holder">
      <h1 class="holder-name">Tessa Virnaud</h1>
      <p class="holder-title">Managing Director</p>
    </header>

    <ul class="contact">
      <li>Migration Agent MARN 0917264</li>
      <li>Postal Address: PO Box 2749</li>
      <li>Carlwood East VIC 3179</li>
      <li>Australia Mobile: 0417296031</li>
      <li class="gap-before">Office address: Level 1, 287 Fenwick Road, Ardmere VIC 3211</li>
      <li>Telephone: 61 3 8714 6023</li>
      <li>Fax + 61 3 8735 2910</li>
      <li>E-mail: tessa@farreachrelocation-example.com</li>
      <li>Web www.farreachrelocation-example.com</li>
    </ul>
  </main>
</body>
</html>
```